依頼概要
◆本のタイトル
港町グラス日記~灯りの奥のササヤキ~

◆著者
桑原 美津江

◆依頼目的/概要
電子書籍を出版しますので、表紙デザイン作成をお願いいたします。

◆デザイン要望
基本的にお任せです。
イラストや写真等素材を使用される場合には、
商用利用可の素材をお願いします。

色合い、デザイン、レイアウトともデザイナーさんにお任せしたいと思います。

※参考として書籍の原稿を添付します。

◆本の内容
ショットバー”ブルクハルモン”のオーナーバーテンダーである私、桑原美津江が実話をもとに店で繰り広げられる様々な人間ドラマを本にしました。
登場人物であるお客様をヒーロー、ヒロインにするつもりで構成しました。
読者が元気や活力を得て、人生を前向きに生きる一助になることを願い、書き進めました。バーという非日常の空間の中で、臨場感や私とお客様とのやりとりがダイレクトに伝わり、読者の様々な感情を揺さぶることができれば、嬉しく思います。

◆読者ターゲット層
〇30代、40代、50代前半までの働く男性、女性
〇自分の生き方や仕事に漠然とした不安や悩みがある人
〇人生を前向きに自分らしく生きたい人
〇職場間、夫婦間、親子間など人間関係にストレスや問題を抱えている人

◆デザイン要望
〇私が女性バーテンダーで、女性のご来店も多いので、女性が一人でも行ってみたいと思わせる雰囲気のデザイン希望です

〇バーというと敷居が高く、入りにくいイメージを持っている人が多いので、品位は保ちつつもあたたかい雰囲気が伝わるようにしていただきたいです

◆写真素材購入の際は別途写真代をお支払いします。その場合は電子書籍ですので、小サイズで結構です。

◆選定確約です。

◆選定デザインの他に、次点、次々点の方にも報酬をご用意しています。

◆その他、デザインに必要な情報がありましたら、お答えします。
遠慮なく聞いてください。
お盆中で、デザイナーさんから締め切り延長のご希望がありましたので、
2日間だけ、延長することになりました。よろしくお願いします。
■ 選んだ理由

赤、黒、白のデザインは、店と私の雰囲気にぴったりで、とても気に入りました。
オビも読者目線で考えていただき、感謝しています。
おしゃれで元気にもになるそんなデザインに感じました。

■ 提案者全員のお礼・コメント

原稿を読んでくださり、それぞれの強い思いでデザインを考えてくださったのが、
伝わってきました。
お一人、お一人に感謝申し上げます。
良いデザインばかりで、選ぶのに正直とても迷いました。
出版の機会がありましたら、またコンペにご参加くださるとありがたいです。
本当にありがとうございました。

```html
<!DOCTYPE html>
<html lang="ja">
<head>
<meta charset="utf-8">
<title>港町グラス日記 ~灯りの奥のササヤキ~ 表紙</title>
<link rel="stylesheet" href="https://fonts.googleapis.com/css2?family=Noto+Sans+JP:wght@700;900&family=Noto+Serif+JP:wght@500;700&display=swap">
<style>
  :root {
    --ink: #0d0b0b;
    --panel: rgba(20, 16, 16, 0.86);
    --white: #ffffff;
    --red: #c9161d;
    --red-deep: #a50f15;
    --glass-top: #dfe8e4;
    --glass-low: #6f8a7c;
    --bar-top: #3a2a1c;
    --bar-low: #8a6a3e;
    --city-top: #1b2233;
    --city-low: #c08a4a;
  }
  * { margin: 0; padding: 0; box-sizing: border-box; }
  html, body { width: 750px; height: 1200px; overflow: hidden; background: var(--ink); }
  .cover { position: relative; width: 750px; height: 1200px; overflow: hidden; background: var(--ink); font-family: "Noto Serif JP", serif; color: var(--white); }

  .photo { position: absolute; }
  .photo-cocktail { left: 0; top: 0; width: 250px; height: 470px; background: linear-gradient(160deg, var(--glass-top) 0%, #a9bfb3 45%, var(--glass-low) 100%); }
  .photo-bar { left: 250px; top: 0; width: 500px; height: 620px; background: linear-gradient(180deg, #2a1e16 0%, var(--bar-top) 40%, var(--bar-low) 100%); }
  .photo-shelves { left: 0; top: 470px; width: 250px; height: 150px; background: linear-gradient(180deg, #5b4630 0%, #2b2018 100%); }
  .photo-city { left: 0; top: 620px; width: 750px; height: 330px; background: linear-gradient(180deg, var(--city-top) 0%, #3a3038 55%, var(--city-low) 100%); }

  .frame { position: absolute; left: 20px; top: 20px; width: 710px; height: 1160px; border: 3px solid var(--white); pointer-events: none; }

  .title-panel { position: absolute; left: 237px; top: 50px; width: 345px; height: 850px; background: var(--panel); }

  .vertical { position: absolute; writing-mode: vertical-rl; text-orientation: upright; white-space: nowrap; }
  .subtitle { left: 262px; top: 62px; font-size: 31px; font-weight: 500; letter-spacing: 2px; }
  .title { left: 360px; top: 78px; font-size: 102px; font-weight: 700; line-height: 1; letter-spacing: 8px; }
  .author-roman { position: absolute; left: 496px; top: 400px; writing-mode: vertical-rl; font-size: 30px; font-style: italic; font-weight: 500; letter-spacing: 1px; white-space: nowrap; }
  .author { left: 515px; top: 640px; font-size: 42px; font-weight: 700; letter-spacing: 4px; }

  .shop-mark { position: absolute; left: 590px; top: 430px; display: flex; align-items: center; gap: 6px; }
  .shop-mark .dot { width: 14px; height: 14px; background: var(--red); }
  .shop-mark .name { font-family: "Noto Serif JP", serif; font-size: 15px; font-weight: 500; letter-spacing: 0; color: var(--white); }

  .obi { position: absolute; left: 0; top: 937px; width: 750px; height: 263px; background: linear-gradient(180deg, var(--red) 0%, var(--red-deep) 100%); }
  .portrait { position: absolute; left: 35px; top: 900px; width: 205px; height: 205px; border-radius: 50%; border: 5px solid var(--white); background: radial-gradient(circle at 50% 40%, #f4e6d6 0%, #d9c2a8 60%, #9a8a7a 100%); }
  .obi-copy { position: absolute; left: 262px; top: 962px; font-family: "Noto Sans JP", sans-serif; font-weight: 900; font-size: 37px; line-height: 54px; color: var(--white); white-space: nowrap; }
</style>
</head>
<body>
  <main class="cover">
    <div class="photo photo-cocktail" role="img" aria-label="ミントとライムを添えたカクテルグラスの写真"></div>
    <div class="photo photo-bar" role="img" aria-label="バーカウンターと棚に並ぶボトルの写真"></div>
    <div class="photo photo-shelves" role="img" aria-label="棚に並ぶ洋酒ボトルの写真"></div>
    <div class="photo photo-city" role="img" aria-label="港町の夜景の写真"></div>

    <section class="title-panel" aria-hidden="true"></section>
    <p class="vertical subtitle">灯りの奥のササヤキ</p>
    <h1 class="vertical title">港町グラス日記</h1>
    <p class="author-roman">Mitsue Kuwahara</p>
    <p class="vertical author">桑原美津江</p>

    <div class="shop-mark">
      <span class="dot"></span>
      <span class="name">BURGHARMON</span>
    </div>

    <section class="obi"></section>
    <div class="portrait" role="img" aria-label="著者の似顔絵イラスト"></div>
    <p class="obi-copy">カクテルを通して繰り<br>広げられる、笑顔と涙<br>あふれる人間ストーリー。</p>

    <div class="frame"></div>
  </main>
</body>
</html>
```